Boost Your Rankings - Search Engine Website

I am launching an SEO website and I am looking to have the site designed. There are a total of 8-10 pages that will need to be designed. I am providing 2 pages off the bat and will work with a designer once these 2 pages are complete. I have never posted a contest for website design (only logos, brochures, etc) so please let me know if there is anything you need from me. I am uploading 2 versions of our logo - a horizontal and a vertical version. I was thinking of getting these rendered in 3d, but I am just going with these for now. I am hoping to complete all work in 10 days, so hopefully the right design for the 1st 2 pages are submitted promptly.

We provide search engine optomization tools and backlinking tools. We provide free research tools as well as cost effective packages for SEO.

I am including 2 word files that have info about the home page and keyword summary page. Additional pages will include: Keyword Research Summary, The Que, Reports, etc.

I am also uploading a zip file that has some examples of home pages that I like. None of them are exactly what I am looking for, but they have certain elements that I like.

I am looking for a clean design and stands out and has good use of color.

Link to instructions files (2...more will be uploaded as first 2 pages are finalized): https://www.filevanta.net/sh/k4m2w7r9x3q5z8/Lp_Tn-7uy2

Forgot to include our logos. Here is a drop box link to the logos: 

https://www.filevanta.net/sh/93jd7fw2mx8qzpa/4Hy_Wq8eTn

big and small businesses, resellers

Seo

• see attached MS Word files for details about requirements.

```html
<!DOCTYPE html>
<html lang="en">
<head>
<meta charset="utf-8">
<title>RankClimb – Search Engine Rankings</title>
<link href="https://fonts.googleapis.com/css2?family=Roboto+Condensed:wght@400;700&family=Open+Sans:wght@400;600&family=Questrial&display=swap" rel="stylesheet">
<style>
:root{
  --ink:#222;
  --blue:#1d6fc4;
  --blue-deep:#0f4f9a;
  --blue-light:#3aa0ea;
  --orange:#f26a1b;
  --orange-text:#f5831f;
  --red:#e8262c;
  --grey-card:#c9c9c9;
  --footer-line:#555;
  --text-grey:#444;
}
*{box-sizing:border-box;margin:0;padding:0}
html,body{width:690px;height:1200px;overflow:hidden}
body{position:relative;background:#fff;font-family:"Questrial",sans-serif;color:var(--ink)}
.abs{position:absolute}

/* header */
.site-header{left:0;top:0;width:690px;height:83px;background:linear-gradient(#2a2a2a,#111)}
.brand{left:14px;top:24px;font:700 32px/1 "Roboto Condensed",sans-serif;color:var(--blue-light);letter-spacing:.5px}
.call{right:14px;top:16px;font:700 19px/1 "Roboto Condensed",sans-serif;color:#fff}
.call span{color:var(--blue-light)}
.social{top:49px;display:flex;align-items:center;gap:3px;font:700 9px/1 "Open Sans",sans-serif}
.social .btn{background:#ddd;color:#333;padding:3px 5px;border-radius:2px}
.social .cnt{background:#fff;color:#333;padding:3px 6px;border-radius:2px}

/* nav */
.main-nav{left:0;top:83px;width:690px;height:45px;background:linear-gradient(var(--blue-light),var(--blue) 60%,var(--blue-deep))}
.main-nav ul{list-style:none;display:flex;height:100%;align-items:center;padding-left:18px}
.main-nav li{font:400 15px/1 "Roboto Condensed",sans-serif;color:#fff}
.login{right:14px;top:93px;width:56px;height:24px;background:linear-gradient(#ffb54a,#f07a12);border-radius:3px;font:700 14px/24px "Roboto Condensed",sans-serif;color:var(--ink);text-align:center}

/* hero */
.hero{left:0;top:128px;width:690px;height:292px;background:radial-gradient(ellipse at 40% 40%,#d98a3e 0%,#8a5a35 45%,#3b2a22 100%)}
.hero-title{left:0;top:145px;width:690px;text-align:center;font:700 22px/1 "Roboto Condensed",sans-serif;color:#fff;text-shadow:0 1px 2px rgba(0,0,0,.5)}
.trial-panel{left:15px;top:188px;width:349px;height:209px;background:rgba(255,255,255,.12);border:1px solid rgba(255,255,255,.18)}
.trial-title{left:54px;top:200px;font:700 21px/1 "Roboto Condensed",sans-serif;color:#fff}
.trial-note{left:56px;top:223px;font:400 8px/1 "Roboto Condensed",sans-serif;color:#fff}
.field{left:56px;width:266px;height:27px;border:1px solid rgba(255,255,255,.7);background:rgba(255,255,255,.2);font:400 12px/25px "Roboto Condensed",sans-serif;color:#fff;padding-left:11px}
.signup{left:56px;top:329px;width:266px;height:43px;background:linear-gradient(#5fb0ec,#1d6fc4);border-radius:2px;text-align:center;color:#fff}
.signup b{display:block;font:700 18px/1 "Roboto Condensed",sans-serif;padding-top:6px}
.signup small{font:400 7px/1 "Roboto Condensed",sans-serif}
.signin{left:56px;top:377px;width:266px;text-align:center;font:400 7.5px/1 "Roboto Condensed",sans-serif;color:#fff}
.hero-art{left:430px;top:186px;width:236px;height:236px;border-radius:6px;background:linear-gradient(160deg,#e6e6e6 0%,#1d5fc4 25%,#1a4fb0 65%,#cfcfcf 80%,#eee 100%)}

/* intro */
.domain-label{left:16px;top:452px;font:400 12.5px/1 "Questrial",sans-serif;color:var(--red)}
.domain-input{left:196px;top:449px;width:195px;height:21px;background:var(--red);font:400 8px/21px "Questrial",sans-serif;color:#fff;padding-left:10px}
.domain-go{left:373px;top:451px;width:16px;height:17px;background:#c81d22}
.why-title{left:14px;top:489px;font:400 15px/1 "Questrial",sans-serif;color:var(--ink)}
.why-text{left:14px;width:412px;font:400 8.6px/15.2px "Questrial",sans-serif;color:var(--text-grey)}
.why-text em{font-style:normal;color:var(--orange-text)}
.read-more{left:378px;top:640px;font:400 7.5px/1 "Open Sans",sans-serif;color:var(--blue-deep)}

/* video */
.player{left:447px;top:449px;width:230px;height:216px;background:#eee;border-radius:3px;box-shadow:0 2px 4px rgba(0,0,0,.3)}
.player-frame{left:447px;top:449px;width:230px;height:172px;background:#1a1a1a;border-radius:3px 3px 0 0}
.player-screen{left:458px;top:460px;width:204px;height:148px;background:linear-gradient(#fafafa,#e9eef2)}

/* cards */
.card{width:206px;height:106px;border-radius:22px 22px 0 22px;background:var(--grey-card)}
.card-head{position:absolute;left:0;top:0;width:100%;height:27px;border-radius:22px 22px 0 0;border-bottom:1px solid rgba(255,255,255,.5);font:400 10.5px/33px "Roboto Condensed",sans-serif;color:var(--ink);padding-left:47px}
.card p{position:absolute;left:14px;top:35px;width:185px;font:400 8.4px/14px "Open Sans",sans-serif;color:var(--ink)}
.card.active{background:linear-gradient(var(--blue),var(--blue-deep))}
.card.active .card-head,.card.active p{color:#fff}
.card-icon{width:42px;height:42px;border-radius:50%;background:#c4c4c4;border:3px solid #fff;display:flex;align-items:center;justify-content:center}
.card-icon.active{background:var(--orange)}

/* footer */
.site-footer{left:0;top:978px;width:690px;height:174px;background:#2e2e2e}
.foot-col h4{font:400 12px/1 "Questrial",sans-serif;color:#fff;margin-bottom:8px}
.foot-col ul{list-style:none}
.foot-col li{font:400 7.5px/1 "Questrial",sans-serif;color:#aaa;padding:5px 0 8px;border-bottom:1px solid var(--footer-line);width:105px}
.blog-date{left:505px;top:1014px;width:50px;height:42px;background:#fff;display:flex}
.blog-date .day{width:16px;background:#f6c70f;font:400 11px/42px "Open Sans",sans-serif;text-align:center;color:var(--ink)}
.blog-date .mon{font:400 8px/12px "Open Sans",sans-serif;color:var(--ink);padding:8px 0 0 6px}
.blog-text{left:560px;top:1013px;width:106px;font:400 8px/12px "Open Sans",sans-serif;color:#fff}
.blog-text a{color:var(--blue);text-decoration:none}
.foot-brand{left:569px;top:1102px;width:110px;text-align:right;font:700 20px/1 "Roboto Condensed",sans-serif;color:#111}
.legal{left:0;top:1152px;width:690px;height:48px;background:#444;text-align:center;font:400 7.5px/13px "Questrial",sans-serif;color:#ddd;padding-top:8px}
.legal b{font-weight:400;color:#fff}
</style>
</head>
<body>

<header class="abs site-header"></header>
<div class="abs brand">RankClimb.net</div>
<div class="abs call"><span>Call:</span> 123.456.789</div>
<div class="abs social" style="left:484px"><span class="btn">+1</span><span class="cnt">0</span></div>
<div class="abs social" style="left:543px"><span class="btn">Post</span><span class="cnt">0</span></div>
<div class="abs social" style="left:620px"><span class="btn">Like</span><span class="cnt">0</span></div>

<nav class="abs main-nav">
  <ul>
    <li style="width:64px">Home</li>
    <li style="width:81px">About Us</li>
    <li style="width:79px">Services</li>
    <li style="width:79px">Features</li>
    <li style="width:89px">Resources</li>
    <li style="width:80px">Free Trial</li>
    <li style="width:54px">FAQ</li>
    <li>Contact Us</li>
  </ul>
</nav>
<div class="abs login">Log in</div>

<section class="abs hero" role="img" aria-label="Blurred office background photo"></section>
<h1 class="abs hero-title">Boost Your Search Engine Rankings Using Legal Back Linking Techniques.</h1>
<div class="abs trial-panel"></div>
<h2 class="abs trial-title">Start Your Free Trail</h2>
<div class="abs trial-note">No Creait card required</div>
<div class="abs field" style="top:247px">Name:</div>
<div class="abs field" style="top:288px">Email:</div>
<div class="abs signup"><b>Sign up for free</b><small>No card details asked</small></div>
<div class="abs signin">Alreday have an account? Sign In</div>
<div class="abs hero-art" role="img" aria-label="Illustration of a desktop monitor showing a globe with a searching banner"></div>

<div class="abs domain-label">Enter your website’s domin:</div>
<div class="abs domain-input">http://www.</div>
<div class="abs domain-go">
  <svg width="16" height="17" viewBox="0 0 16 17"><circle cx="7" cy="7.5" r="3.5" fill="none" stroke="#fff" stroke-width="1.6"/><line x1="9.6" y1="10.2" x2="12.5" y2="13.2" stroke="#fff" stroke-width="1.8"/></svg>
</div>

<h2 class="abs why-title">Why Choose RankClimb?</h2>
<p class="abs why-text" style="top:514px"><em>Lorem ipsum dolor sit amet,</em> consectetur adipiscing elit. Fusce hendrerit ante vitae nisl iaculis porta. Etiam ac nunc ante, quis aliquam turpis. Duis sollicitudin nibh eu turpis rhoncus vitae sodales risus auctor. Nulla id consequat sapien. Nulla facilisi. Duis sem ligula, viverra id commodo at, dictum non est. Mauris sed lacus vel dolor luctus porta. Mauris at nulla risus, ac pretium dolor.</p>
<p class="abs why-text" style="top:581px">Maecenas eu nisi purus. Lorem ipsum dolor sit amet, <em>consectetur adipiscing elit. In sit amet</em> neque nec risus mollis hendrerit. Nam vitae felis ut erat convallis imperdiet. In hac habitasse platea dictumst. Sed nec diam justo. Vestibulum at libero eget magna imperdiet ultrices non et dolor. Sed euismod, orci quis iaculis mattis, leo dolor elementum enim, ut posuere odio enim in ante.</p>
<div class="abs read-more">Read more »</div>

<div class="abs player"></div>
<div class="abs player-frame"></div>
<div class="abs player-screen" role="img" aria-label="Illustrated presenter pointing at a rising line chart"></div>
<svg class="abs" style="left:458px;top:595px" width="204" height="80" viewBox="0 0 204 80">
  <rect x="12" y="4" width="182" height="5" rx="2.5" fill="#333"/>
  <rect x="12" y="4" width="108" height="5" rx="2.5" fill="#d01c1c"/>
  <circle cx="119" cy="6.5" r="5" fill="#eee" stroke="#888"/>
  <circle cx="7" cy="46" r="5" fill="none" stroke="#555" stroke-width="3" stroke-dasharray="2.5 1.5"/>
  <path d="M67 40v12M77 40l-8 6 8 6z" fill="#555" stroke="#555" stroke-width="2"/>
  <circle cx="103" cy="46" r="14" fill="#f4f4f4" stroke="#bbb"/>
  <rect x="98" y="40" width="3" height="12" fill="#444"/><rect x="105" y="40" width="3" height="12" fill="#444"/>
  <path d="M131 40l8 6-8 6zM140 40v12" fill="#555" stroke="#555" stroke-width="2"/>
  <rect x="164" y="42" width="11" height="8" fill="none" stroke="#555" stroke-width="1.6"/>
  <path d="M195 42h3l5-4v16l-5-4h-3z" fill="#555"/>
</svg>

<div class="abs card active" style="left:14px;top:714px"><div class="card-head">SEO Basics</div><p>Curabitur egestas elit eget nunc eleifend bibendum. Integer iaculis, erat volutpat posu aliquet, urna velit auctor turpis, in consectetur leo magna eu enim.</p></div>
<div class="abs card" style="left:242px;top:714px"><div class="card-head">SEO Tips</div><p>Curabitur egestas elit eget nunc eleifend bibendum. Integer iaculis, erat volutpat posu aliquet, urna velit auctor turpis, in consectetur leo magna eu enim.</p></div>
<div class="abs card" style="left:470px;top:714px"><div class="card-head">Tips To Using Our System</div><p>Curabitur egestas elit eget nunc eleifend bibendum. Integer iaculis, erat volutpat posu aliquet, urna velit auctor turpis, in consectetur leo magna eu enim.</p></div>
<div class="abs card" style="left:14px;top:856px"><div class="card-head">Free Keyword Analysis Tools</div><p>Curabitur egestas elit eget nunc eleifend bibendum. Integer iaculis, erat volutpat posu aliquet, urna velit auctor turpis, in consectetur leo magna eu enim.</p></div>
<div class="abs card" style="left:242px;top:856px"><div class="card-head">What To Expect</div><p>Curabitur egestas elit eget nunc eleifend bibendum. Integer iaculis, erat volutpat posu aliquet, urna velit auctor turpis, in consectetur leo magna eu enim.</p></div>
<div class="abs card" style="left:470px;top:856px"><div class="card-head">White Label</div><p>Curabitur egestas elit eget nunc eleifend bibendum. Integer iaculis, erat volutpat posu aliquet, urna velit auctor turpis, in consectetur leo magna eu enim.</p></div>

<div class="abs card-icon active" style="left:13px;top:685px"><svg width="20" height="16" viewBox="0 0 20 16"><path d="M1 1v14h18" fill="none" stroke="#fff" stroke-width="1.6"/><path d="M4 11l4-5 3 3 5-6" fill="none" stroke="#fff" stroke-width="1.8"/></svg></div>
<div class="abs card-icon" style="left:241px;top:685px"><svg width="14" height="20" viewBox="0 0 14 20"><path d="M7 1a6 6 0 0 0-3.5 10.9V14h7v-2.1A6 6 0 0 0 7 1z" fill="none" stroke="#555" stroke-width="1.6"/><rect x="4" y="16" width="6" height="2.5" fill="#555"/></svg></div>
<div class="abs card-icon" style="left:469px;top:685px"><svg width="22" height="18" viewBox="0 0 22 18"><rect x="1" y="1" width="20" height="12" fill="#555"/><rect x="8" y="14" width="6" height="2" fill="#555"/><rect x="5" y="16" width="12" height="1.6" fill="#555"/></svg></div>
<div class="abs card-icon" style="left:13px;top:827px"><svg width="20" height="20" viewBox="0 0 20 20"><rect x="1.5" y="3.5" width="14" height="15" fill="none" stroke="#555" stroke-width="2"/><path d="M8 12l9-9 2 2-9 9H8z" fill="#555"/></svg></div>
<div class="abs card-icon" style="left:241px;top:827px"><svg width="22" height="20" viewBox="0 0 22 20"><circle cx="8" cy="8" r="4" fill="#555"/><path d="M1 19a7 6 0 0 1 14 0z" fill="#555"/><path d="M13 2h8v5h-5l-2 2v-2h-1z" fill="#555"/></svg></div>
<div class="abs card-icon" style="left:469px;top:827px"><svg width="16" height="20" viewBox="0 0 16 20"><path d="M1 1h14v13l-5 5H1z" fill="#555"/></svg></div>

<footer class="abs site-footer"></footer>
<div class="abs foot-col" style="left:14px;top:988px"><h4>Company</h4><ul><li>About Us</li><li>Why Choose</li><li>RankClimb</li><li>Affiliate Program</li><li>Tips To Using Our System</li><li>FAQ</li></ul></div>
<div class="abs foot-col" style="left:179px;top:988px"><h4>Company</h4><ul><li>Link Building</li><li>Local SEO</li><li>Free Trial</li><li>Free Keyword Analysis Tools</li><li>VidStream Video Marketing</li></ul></div>
<div class="abs foot-col" style="left:366px;top:988px"><h4>SEO</h4><ul><li style="width:60px">SEO Basics</li><li style="width:60px">SEO Tips</li><li style="width:60px">On page SEO</li><li style="width:60px">Off page SEO</li></ul></div>
<div class="abs foot-col" style="left:505px;top:989px"><h4>Blog</h4></div>
<div class="abs blog-date"><div class="day">01</div><div class="mon">Feb<br>2013</div></div>
<div class="abs blog-text">Lorem ipsum dolor sit amet, consectetur adipiscing elit. Praesent a libero<br><a>Read more »</a></div>
<div class="abs foot-brand">RankClimb</div>

<div class="abs legal">Copyright© 2013 RankClimb use of this website consittues acceptance our <b>user agreement</b> and <b>privacy policy</b><br>*condition apply please see our <b>money back refund policy</b></div>

</body>
</html>
```